依頼詳細
そこを通れば見落とさずに、入ってこれるような、目立つ看板で、それなりにカッコいいけど親しみやすい雰囲気がいいです。
サイズは縦長で、縦360cm×横90cmです。
記載項目
タイドオービット、Tide Orbit、株式会社アウルリード、Owl-Reed
希望イメージ
シンプル 複雑
単色 カラフル
暗い 明るい
日常 高級
遊び心 厳粛
未来的 伝統的
女性的 男性的
希望する色
赤系、緑系、黄・オレンジ系
納品ファイル
• 高解像度JPG (.jpg)
• イラストレーター形式 (.ai)
• フォトショップ形式 (.psd)
補足説明
イメージカラーは明るい緑とオレンジです。
会社のロゴは添付の通りなので、そのOwl-Reedの部分を、Tide Orbit/タイドオービットにして、その下に「Produced by Owl-Reed Inc」というように入れて使ってもらいたいです。
ロゴを添付します

```html
<!DOCTYPE html>
<html lang="ja">
<head>
<meta charset="utf-8">
<title>Tide Orbit ミニバン専門店 縦看板</title>
<link rel="stylesheet" href="https://fonts.googleapis.com/css2?family=M+PLUS+Rounded+1c:wght@500;800&display=swap">
<style>
  :root {
    --paper: #ffffff;
    --frame: #1e1e1e;
    --orange: #e8913a;
    --orange-soft: #f2c08e;
    --charcoal: #3a3f44;
    --gray: #8c8c8c;
  }
  html, body {
    margin: 0;
    padding: 0;
    width: 1200px;
    height: 4196px;
    overflow: hidden;
    background: var(--paper);
  }
  .signboard {
    position: relative;
    width: 1200px;
    height: 4196px;
    background: var(--paper);
    font-family: "M PLUS Rounded 1c", sans-serif;
    color: var(--charcoal);
  }
  .signboard__frame {
    position: absolute;
    left: 100px;
    top: 88px;
    width: 1000px;
    height: 3980px;
    border: 4px solid var(--frame);
    box-sizing: border-box;
    overflow: hidden;
    background: var(--paper);
  }
  .brand {
    position: absolute;
    left: 76px;
    top: 1230px;
    width: 850px;
  }
  .brand__mark {
    width: 220px;
    height: 220px;
    background: var(--orange);
    margin-bottom: 160px;
  }
  .brand__name {
    margin: 0;
    font-weight: 800;
    font-size: 300px;
    line-height: 230px;
    letter-spacing: -6px;
    color: var(--charcoal);
    white-space: nowrap;
  }
  .brand__kana {
    margin: 40px 0 0 6px;
    font-weight: 500;
    font-size: 48px;
    line-height: 1.2;
    letter-spacing: 2px;
  }
  .brand__producer {
    margin: 4px 0 0 6px;
    font-weight: 800;
    font-size: 72px;
    line-height: 1.2;
    white-space: nowrap;
  }
  .shop-type {
    margin: 30px 0 0 0;
    width: 850px;
    text-align: center;
    font-weight: 800;
    font-size: 112px;
    line-height: 1.25;
    letter-spacing: 2px;
    white-space: nowrap;
  }
  .decor-field {
    position: absolute;
    left: 0;
    bottom: 0;
    width: 992px;
    height: 1150px;
    display: block;
  }
</style>
</head>
<body>
  <div class="signboard">
    <div class="signboard__frame">
      <div class="brand">
        <div class="brand__mark"></div>
        <h1 class="brand__name">Tide<br>Orbit</h1>
        <p class="brand__kana">タイドオービット</p>
        <p class="brand__producer">Produced By Owl-Reed</p>
        <p class="shop-type">ミニバン専門店</p>
      </div>
      <svg class="decor-field" viewBox="0 0 992 1150" preserveAspectRatio="none" role="img" aria-label="オレンジとグレーの大きな六角形が斜めに並ぶ装飾パターン">
        <defs>
          <linearGradient id="decorTone" x1="0" y1="0" x2="1" y2="1">
            <stop offset="0" stop-color="#f2c08e"/>
            <stop offset="0.55" stop-color="#f2c08e"/>
            <stop offset="1" stop-color="#8c8c8c"/>
          </linearGradient>
        </defs>
        <path d="M0 60 L300 0 L560 160 L992 280 L992 1150 L0 1150 Z" fill="url(#decorTone)"/>
      </svg>
    </div>
  </div>
</body>
</html>
```